luxury contemporary fashion website needs simple, elegant flowchart to describe the buying and selli

* Luxury, resale, preloved items are sold on this online platform
*Horizontal, simple, flowchart with 5 steps in 'friendly' font with a simple emoticon/ picture for each step
*To be positioned in the 'How we work' tab of the webpage to explain in a very simple manner the buying and selling process for the customers.
*Attached is a very rudimentary mock-up of what we would like included and an idea of a project similar to what we desire
* to confirm the text for each step, we have also attached a word file below

Industry/Entity Type

Fashion

Font styles to use
Sans Serif

Colors
86cfc6
cfeae6

Requirements
Must have
• Simple drawing / shape after each point In the closest to 'duck egg blue' fill colour you can find with a black outline

```html
<!DOCTYPE html>
<html lang="en">
<head>
<meta charset="utf-8">
<title>How we work</title>
<link rel="stylesheet" href="https://fonts.googleapis.com/css2?family=Playball&family=Parisienne&display=swap">
<style>
  :root {
    --duck-egg: #86cfc6;
    --duck-egg-pale: #cfeae6;
    --ink: #111111;
    --paper: #ffffff;
    --heart: #d8283a;
  }
  * { margin: 0; padding: 0; box-sizing: border-box; }
  html, body { width: 1200px; height: 1000px; overflow: hidden; background: var(--paper); }
  .flowchart { position: relative; width: 1200px; height: 1000px; }
  .connectors, .icons { position: absolute; inset: 0; width: 1200px; height: 1000px; }
  .step-title, .step-note, .step-number, .payment-title {
    position: absolute; white-space: nowrap; transform: translateX(-50%);
  }
  .step-title {
    font-family: "Playball", cursive;
    font-size: 44px; line-height: 1;
    color: var(--duck-egg);
    -webkit-text-stroke: 0.6px #6fb9b0;
  }
  .step-note {
    font-family: "Parisienne", cursive;
    font-size: 20px; line-height: 1;
    color: var(--ink);
  }
  .step-number {
    width: 44px; height: 44px; border-radius: 50%;
    background: var(--ink); color: var(--paper);
    font-family: "Parisienne", cursive; font-size: 28px;
    display: flex; align-items: center; justify-content: center;
    transform: translate(-50%, -50%);
  }
  .payment-number {
    background: transparent; border: 3px solid var(--paper);
    width: 40px; height: 40px; font-size: 26px;
  }
  .payment-title {
    font-family: "Playball", cursive; font-size: 42px; color: var(--paper);
  }
  .currency {
    position: absolute; font-family: "Playball", cursive; font-weight: 700;
    color: var(--duck-egg); -webkit-text-stroke: 2px var(--ink); line-height: 1;
  }
  .charity-icon {
    position: absolute; left: 1000px; top: 752px; width: 80px; height: 84px;
    border-radius: 50%; background: var(--duck-egg); border: 4px solid var(--ink);
  }
</style>
</head>
<body>
<main class="flowchart">
  <svg class="connectors" viewBox="0 0 1200 1000" aria-hidden="true">
    <g fill="none" stroke="var(--ink)" stroke-linecap="round">
      <path d="M300 160 C 470 115, 700 118, 858 156" stroke-width="4"/>
      <path d="M845 145 L860 158 L842 162" stroke-width="2"/>
      <path d="M740 214 C 700 218, 660 232, 642 256" stroke-width="6"/>
      <path d="M640 244 L640 260 L656 258" stroke-width="2"/>
      <path d="M728 322 C 760 380, 745 440, 702 470" stroke-width="6"/>
      <path d="M700 456 L700 472 L716 470" stroke-width="2"/>
      <path d="M520 518 C 460 540, 428 590, 428 645" stroke-width="6"/>
      <path d="M420 632 L428 648 L436 632" stroke-width="2"/>
      <path d="M414 700 C 380 640, 320 605, 242 602" stroke-width="6"/>
      <path d="M254 592 L240 602 L252 612" stroke-width="2"/>
      <path d="M790 712 C 830 650, 890 615, 963 616" stroke-width="6"/>
      <path d="M950 606 L965 616 L951 626" stroke-width="2"/>
    </g>
    <g class="cloud" fill="var(--duck-egg)">
      <circle cx="520" cy="690" r="75"/>
      <circle cx="615" cy="665" r="75"/>
      <circle cx="705" cy="695" r="70"/>
      <rect x="428" y="690" width="352" height="118" rx="55"/>
    </g>
    <g fill="none" stroke="var(--paper)" stroke-width="3">
      <path d="M470 660 C 490 630, 530 620, 560 630"/>
      <path d="M580 620 C 610 600, 660 605, 680 630"/>
      <path d="M700 650 C 730 640, 760 660, 765 685"/>
    </g>
  </svg>

  <svg class="icons" viewBox="0 0 1200 1000" aria-hidden="true">
    <g fill="var(--duck-egg)" stroke="var(--ink)" stroke-width="2" stroke-linejoin="round">
      <path d="M398 287 L408 312 L435 313 L414 330 L421 356 L398 341 L375 356 L382 330 L361 313 L388 312 Z"/>
      <path d="M438 280 L443 292 L456 293 L446 301 L449 314 L438 307 L427 314 L430 301 L420 293 L433 292 Z"/>
      <path d="M458 270 L461 278 L469 278 L463 283 L465 291 L458 286 L451 291 L453 283 L447 278 L455 278 Z"/>
      <circle cx="494" cy="441" r="11" stroke-width="2.5"/>
      <line x1="486" y1="450" x2="475" y2="468" stroke-width="4"/>
      <rect x="512" y="440" width="44" height="34"/>
      <rect x="509" y="432" width="50" height="10"/>
      <line x1="534" y1="432" x2="534" y2="474"/>
      <path d="M534 432 C 520 418, 514 428, 534 432 C 548 418, 554 428, 534 432"/>
      <path d="M776 633 L828 602 C 834 598, 840 604, 834 609 L784 638 Z"/>
      <path d="M800 620 L794 598 L802 596 L814 612 Z"/>
      <path d="M790 628 L800 650 L807 647 L805 624 Z"/>
    </g>
    <path d="M1030 325 C 1000 305, 1014 285, 1030 300 C 1046 285, 1060 305, 1030 325 Z" fill="var(--heart)"/>
  </svg>

  <section class="step step-1">
    <div class="step-number" style="left:265px; top:172px;">1</div>
    <h2 class="step-title" style="left:285px; top:198px;">Have items to sell?</h2>
    <p class="step-note" style="left:285px; top:264px;">Brand Spanking or neary new</p>
  </section>

  <section class="step step-2">
    <div class="step-number" style="left:930px; top:170px;">2</div>
    <h2 class="step-title" style="left:922px; top:200px;">Personal collection</h2>
    <p class="step-note" style="left:935px; top:257px;">We chose te pieces we know the velora</p>
    <p class="step-note" style="left:890px; top:286px;">customers will love</p>
  </section>

  <section class="step step-3">
    <div class="step-number" style="left:612px; top:262px;">3</div>
    <h2 class="step-title" style="left:610px; top:296px;">We Prepare</h2>
    <p class="step-note" style="left:585px; top:344px;">your item for sale with thorough</p>
    <p class="step-note" style="left:585px; top:372px;">authenticity &amp; condition checks...</p>
    <p class="step-note" style="left:585px; top:400px;">so you dont have to</p>
  </section>

  <section class="step step-4">
    <div class="step-number" style="left:635px; top:488px;">4</div>
    <h2 class="step-title" style="left:600px; top:503px;">Once sold</h2>
    <p class="step-note" style="left:640px; top:547px;">We lovingly prepare the item which</p>
    <p class="step-note" style="left:640px; top:577px;">is shipped via our tracked services</p>
  </section>

  <section class="step step-5">
    <div class="step-number payment-number" style="left:597px; top:688px;">5</div>
    <h2 class="payment-title" style="left:592px; top:716px;">Your payment</h2>
  </section>

  <section class="outcome outcome-cash">
    <h2 class="step-title" style="left:155px; top:633px;">Pocket</h2>
    <h2 class="step-title" style="left:227px; top:678px;">the cash</h2>
    <span class="currency" style="left:150px; top:735px; font-size:60px;">£</span>
    <span class="currency" style="left:215px; top:765px; font-size:66px;">$</span>
    <span class="currency" style="left:272px; top:730px; font-size:60px;">€</span>
  </section>

  <section class="outcome outcome-charity">
    <h2 class="step-title" style="left:1042px; top:606px;">Donate</h2>
    <h2 class="step-title" style="left:1048px; top:646px;">to charity</h2>
    <p class="step-note" style="left:1025px; top:704px;">Full or partial amount</p>
    <div class="charity-icon" role="img" aria-label="Round duck-egg blue charity emoticon with a halo"></div>
  </section>
</main>
</body>
</html>
```